Very visible CoWorking Building Sign overlooking downtown LA and 110 freeway

Our building is drab but very visible and in the best location. We need a great sign for our monolith that overlooks downtown LA and the 100 freeway. We are a new CoWorking business and would like to have a few things we do on the sign: private offices, virtual offices, CoWorking Lounge. Everything we have seen is ho-hum. Can you get us noticed? We need people to know what we do and that we are here but in a creative, professional, unique sign.
Target Market(s)
People who have a business in DTLA, remote workers and those who work from home who need a professional address.
Requirements
Must have
- Our logo (which can be somewhat reimagined) which has our address 2740 on it. The three things we focus on: Private Offices, Virtual Offices, CoWorking Lounge. Incorporate some Navy. Readable from several hundred feet away.
Nice to have
- Mural feel? Something inspirational in this crazy COVID times? Graphics? Color block. I like the idea of decorative but it has to be readable as a building sign. The same with the use of colors. Our colors are grays and navy but with a pop of the chartreuse (we have 2 velvet chartreuse chairs in the space). Helpful to view our website: Halvorn2740.com.
Should not have
- Not too graffiti. Keep it professional but unique and wow.

```html
<!DOCTYPE html>
<html lang="en">
<head>
<meta charset="utf-8">
<title>Halvorn 2740 – Building Sign</title>
<link rel="stylesheet" href="https://fonts.googleapis.com/css2?family=Montserrat:wght@600&display=swap">
<style>
  :root {
    --navy: #003f7d;
    --navy-deep: #17305e;
    --chartreuse: #9aca3c;
    --ring-gray: #c9c9c9;
    --sign-white: #ffffff;
    --sign-mist: #f1f1f1;
    --page-light: #fbfbfb;
    --page-dark: #cfcfcf;
  }
  * { margin: 0; padding: 0; box-sizing: border-box; }
  html, body { width: 1200px; height: 960px; overflow: hidden; }
  body {
    background: linear-gradient(120deg, var(--page-light) 0%, #ececec 55%, var(--page-dark) 100%);
    display: flex;
    align-items: center;
    justify-content: center;
  }
  .building-sign {
    width: 1100px;
    height: 183px;
    display: block;
    box-shadow: 0 6px 18px rgba(0,0,0,0.12);
  }
  .sign-name {
    font-family: "Montserrat", sans-serif;
    font-weight: 600;
    fill: var(--navy-deep);
  }
  .service-label {
    font-family: "Montserrat", sans-serif;
    font-weight: 600;
    fill: var(--sign-white);
    font-size: 44px;
  }
</style>
</head>
<body>
  <svg class="building-sign" viewBox="0 0 1910 318" xmlns="http://www.w3.org/2000/svg" aria-label="Halvorn 2740 building sign: private offices, virtual offices, coworking lounge">
    <defs>
      <linearGradient id="sign-base" x1="0" y1="0" x2="1" y2="1">
        <stop offset="0" stop-color="var(--sign-mist)"/>
        <stop offset="1" stop-color="var(--sign-white)"/>
      </linearGradient>
      <clipPath id="sign-edge">
        <rect width="1910" height="318"/>
      </clipPath>
    </defs>

    <rect class="sign-base" width="1910" height="318" fill="url(#sign-base)"/>

    <g clip-path="url(#sign-edge)">
      <!-- brand roundel -->
      <circle class="brand-ring" cx="478" cy="-100" r="441" fill="var(--chartreuse)"/>
      <circle class="brand-field" cx="478" cy="-100" r="398" fill="var(--sign-white)"/>

      <!-- services arch -->
      <circle class="services-ring" cx="1383" cy="342" r="508" fill="var(--ring-gray)"/>
      <circle class="services-field" cx="1383" cy="342" r="463" fill="var(--navy)"/>
    </g>

    <!-- brand name -->
    <g class="brand-name">
      <circle cx="215" cy="170" r="22" fill="var(--chartreuse)"/>
      <text class="sign-name" x="258" y="155" font-size="46">2740</text>
      <text class="sign-name" x="256" y="228" font-size="84" letter-spacing="4">HALVORN</text>
    </g>

    <!-- services list -->
    <g class="service-list">
      <g class="service-item" transform="translate(1073 36)">
        <path d="M0 0 H58 L80 34 L58 68 H0 Z" fill="var(--chartreuse)"/>
        <path d="M58 0 L80 34 L58 68" fill="none" stroke="var(--sign-white)" stroke-width="3"/>
        <path d="M22 36 L31 46 L47 22" fill="none" stroke="var(--sign-white)" stroke-width="4" stroke-linecap="round" stroke-linejoin="round"/>
      </g>
      <text class="service-label" x="1188" y="86">PRIVATE OFFICES</text>

      <g class="service-item" transform="translate(1073 126)">
        <path d="M0 0 H58 L80 34 L58 68 H0 Z" fill="var(--chartreuse)"/>
        <path d="M58 0 L80 34 L58 68" fill="none" stroke="var(--sign-white)" stroke-width="3"/>
        <path d="M22 36 L31 46 L47 22" fill="none" stroke="var(--sign-white)" stroke-width="4" stroke-linecap="round" stroke-linejoin="round"/>
      </g>
      <text class="service-label" x="1192" y="176">VIRTUAL OFFICES</text>

      <g class="service-item" transform="translate(1073 216)">
        <path d="M0 0 H58 L80 34 L58 68 H0 Z" fill="var(--chartreuse)"/>
        <path d="M58 0 L80 34 L58 68" fill="none" stroke="var(--sign-white)" stroke-width="3"/>
        <path d="M22 36 L31 46 L47 22" fill="none" stroke="var(--sign-white)" stroke-width="4" stroke-linecap="round" stroke-linejoin="round"/>
      </g>
      <text class="service-label" x="1189" y="266">COWORKING LOUNGE</text>
    </g>
  </svg>
</body>
</html>
```